Creative Brief
Stationery and Cards
Need clean, simple, modern cards/letterhead
Simple
Dale Pruett
Executive Direstor
418 Hollister Avenue
Suite 500
New York, NY 10012
Dpruett@brimlow.com
www.mistvaleloft.com

```html
<!DOCTYPE html>
<html lang="en">
<head>
<meta charset="utf-8">
<title>Mistvale Loft Stationery</title>
<link href="https://fonts.googleapis.com/css2?family=Montserrat:wght@400;600&display=swap" rel="stylesheet">
<style>
  :root {
    --board: #3b3b3d;
    --paper: #ffffff;
    --sky: #3cb6e3;
    --leaf: #8cc63f;
    --ink: #5a5f66;
    --muted: #9aa1a8;
    --label: #b9bcc0;
    --shade: rgba(0,0,0,.35);
  }
  * { box-sizing: border-box; margin: 0; padding: 0; }
  html, body { width: 1200px; height: 338px; overflow: hidden; }
  body { background: var(--board); font-family: "Montserrat", Arial, sans-serif; position: relative; }
  .piece { position: absolute; background: var(--paper); box-shadow: 0 2px 6px var(--shade); overflow: hidden; }
  .label { position: absolute; font-size: 5px; color: var(--label); letter-spacing: .2px; text-align: center; }
  .brand { display: flex; flex-direction: column; align-items: center; gap: 2px; }
  .brand-dot { width: 8px; height: 8px; border-radius: 50%; background: var(--sky); }
  .brand-name { font-weight: 600; color: var(--ink); text-transform: uppercase; font-size: 5px; letter-spacing: .8px; }
  .band { position: absolute; left: 0; right: 0; background: var(--sky); }
  .tiny { font-size: 3px; color: var(--muted); line-height: 1.4; }

  /* business cards */
  .card { left: 26px; width: 60px; height: 30px; }
  .card-front { top: 132px; }
  .card-back { top: 192px; }
  .card .brand { position: absolute; left: 6px; top: 7px; }
  .card-back .contact { position: absolute; right: 4px; top: 8px; text-align: right; }

  /* letterheads */
  .letterhead { top: 19px; width: 146px; height: 288px; }
  .letterhead-first { left: 233px; }
  .letterhead-second { left: 396px; }
  .letterhead .band-top { top: 0; height: 4px; }
  .letterhead .band-bottom { bottom: 0; height: 4px; }
  .letterhead .brand { position: absolute; left: 40px; top: 12px; }
  .letterhead .address { position: absolute; right: 10px; top: 14px; text-align: right; }
  .letterhead .footer { position: absolute; left: 0; right: 0; bottom: 8px; text-align: center; }

  /* compliment cards */
  .slip { left: 629px; width: 163px; height: 103px; }
  .slip-front { top: 53px; }
  .slip-back { top: 180px; }
  .slip .band-top { top: 0; height: 5px; }
  .slip .band-bottom { bottom: 0; height: 5px; }
  .slip .brand { position: absolute; left: 0; right: 0; top: 34px; }
  .slip .brand-name { font-size: 6px; }
  .slip .lines { position: absolute; left: 0; right: 0; top: 62px; text-align: center; }

  /* envelopes */
  .envelope { left: 893px; width: 283px; }
  .envelope-sky { top: 24px; height: 67px; background: var(--sky); }
  .envelope-leaf { top: 96px; height: 67px; background: var(--leaf); }
  .envelope-plain { top: 168px; height: 120px; }
  .envelope svg { position: absolute; inset: 0; width: 100%; height: 100%; }
</style>
</head>
<body>

  <!-- business cards -->
  <div class="piece card card-front">
    <div class="brand"><span class="brand-dot"></span><span class="brand-name">Mistvale</span></div>
    <div class="band" style="bottom:0;height:3px"></div>
  </div>
  <div class="label" style="left:26px;top:164px;width:60px">Business Card Front</div>

  <div class="piece card card-back">
    <div class="brand"><span class="brand-dot"></span><span class="brand-name">Mistvale</span></div>
    <div class="contact tiny">Dale Pruett<br>Executive Director<br>Dpruett@brimlow.com<br>www.mistvaleloft.com</div>
    <div class="band" style="bottom:0;height:3px"></div>
  </div>
  <div class="label" style="left:26px;top:224px;width:60px">Business Card Back</div>

  <!-- letterheads -->
  <div class="piece letterhead letterhead-first">
    <div class="band band-top"></div>
    <div class="brand"><span class="brand-dot"></span><span class="brand-name">Mistvale</span></div>
    <div class="address tiny">418 Hollister Avenue<br>Suite 500<br>New York, NY 10012</div>
    <div class="footer tiny">Dpruett@brimlow.com &nbsp;·&nbsp; www.mistvaleloft.com</div>
    <div class="band band-bottom"></div>
  </div>
  <div class="label" style="left:233px;top:310px;width:146px">Letterhead First Page</div>

  <div class="piece letterhead letterhead-second">
    <div class="band band-top"></div>
    <div class="brand"><span class="brand-dot"></span><span class="brand-name">Mistvale</span></div>
    <div class="footer tiny">418 Hollister Avenue, Suite 500, New York, NY 10012</div>
    <div class="band band-bottom"></div>
  </div>
  <div class="label" style="left:396px;top:310px;width:146px">Letterhead Second Page</div>

  <!-- compliment cards -->
  <div class="piece slip slip-front">
    <div class="band band-top"></div>
    <div class="brand"><span class="brand-dot"></span><span class="brand-name">Mistvale</span></div>
    <div class="band band-bottom"></div>
  </div>
  <div class="label" style="left:629px;top:159px;width:163px">Compliment Card Front</div>

  <div class="piece slip slip-back">
    <div class="band band-top"></div>
    <div class="brand"><span class="brand-dot"></span><span class="brand-name">Mistvale</span></div>
    <div class="lines tiny">418 Hollister Avenue · New York, NY 10012<br>www.mistvaleloft.com</div>
    <div class="band band-bottom"></div>
  </div>
  <div class="label" style="left:629px;top:286px;width:163px">Compliment Card Back</div>

  <!-- envelopes -->
  <div class="piece envelope envelope-sky">
    <svg viewBox="0 0 283 67" preserveAspectRatio="none"><polyline points="0,0 141.5,40 283,0" fill="none" stroke="rgba(255,255,255,.35)" stroke-width="1"/></svg>
  </div>
  <div class="piece envelope envelope-leaf">
    <svg viewBox="0 0 283 67" preserveAspectRatio="none"><polyline points="0,0 141.5,40 283,0" fill="none" stroke="rgba(255,255,255,.35)" stroke-width="1"/></svg>
  </div>
  <div class="piece envelope envelope-plain">
    <svg viewBox="0 0 283 120" preserveAspectRatio="none">
      <polyline points="0,0 141.5,62 283,0" fill="none" stroke="#d6d9dc" stroke-width="1"/>
      <polyline points="0,120 110,58" fill="none" stroke="#e2e4e6" stroke-width="1"/>
      <polyline points="283,120 173,58" fill="none" stroke="#e2e4e6" stroke-width="1"/>
    </svg>
  </div>
  <div class="label" style="left:893px;top:293px;width:283px">Envelope Set Colors</div>

</body>
</html>
```